Business Card Design

Carl Benson Insurance Agency, an Independent Insurance Agency which was stated on Orchard Lane in Laplace, Louisiana on 1958 and has grown the six locations throughout South Louisiana. We sell personal (auto Homeowners flood, liability) and commercial insurance (commercial property, general liability, workers compensation, commercial auto). I am looking for a double sided card with list the five remaining locations on the back or maybe even a folded four sided card. Our home office is a two story building with a green roof. I have had a logo designed which I have attached. Open for revisions but would like to stay with in the same green roof over an M. I have attached the logo but can not tell if I was uploaded.

Target Market(s)

Individual and commercial insurance buyers. Upper income and business owners

Industry/Entity Type

Insurance

Requirements
Must have
• Must have similar logo as uploaded. Green roof over M or something similar. List all location address and phone numbers.

Employee name, office phone number; direct phone line; email address and website list all locations on card. Very Similar colors to current logo.
Nice to have
• Possible folded card with double sided print

```html
<!DOCTYPE html>
<html lang="en">
<head>
<meta charset="utf-8">
<title>Carl Benson Insurance Agency – Business Card</title>
<link href="https://fonts.googleapis.com/css2?family=Roboto+Condensed:wght@700&family=Roboto:wght@300;400&display=swap" rel="stylesheet">
<style>
  :root {
    --page: #ecebe8;
    --card: #ffffff;
    --green: #1b6a4b;
    --green-dark: #175c41;
    --blue: #1a86c8;
    --blue-dark: #1666a8;
    --text-light: #ffffff;
    --tagline: #5b6b66;
  }
  * { margin: 0; padding: 0; box-sizing: border-box; }
  html, body { width: 1200px; height: 858px; overflow: hidden; background: var(--page); }
  .canvas {
    position: relative; width: 1200px; height: 858px;
    display: flex; align-items: center; justify-content: center; gap: 40px;
  }
  .card {
    position: relative; width: 540px; height: 309px;
    background: var(--card);
    box-shadow: 0 6px 18px rgba(0,0,0,.18);
    overflow: hidden;
  }
  .card__bands { position: absolute; inset: 0; }

  .brand { position: absolute; display: flex; align-items: center; gap: 10px; }
  .brand__mark { width: 16px; height: 16px; background: var(--green); flex: none; }
  .brand__name {
    font-family: "Roboto Condensed", sans-serif; font-weight: 700;
    color: var(--green); text-transform: uppercase; line-height: 1.02;
  }
  .brand__tagline {
    position: absolute; font-family: "Roboto Condensed", sans-serif; font-weight: 700;
    color: var(--tagline);
  }

  /* front */
  .card--front .brand { left: 28px; top: 118px; }
  .card--front .brand__name { font-size: 24px; width: 210px; }
  .card--front .brand__tagline { left: 54px; top: 178px; font-size: 11.5px; }

  .contact { position: absolute; font-family: "Roboto", sans-serif; font-weight: 300; color: var(--text-light); }
  .contact__name { right: 34px; top: 24px; font-size: 22px; text-align: right; }
  .contact__phones { right: 34px; top: 60px; font-size: 14px; line-height: 22px; }
  .contact__online { right: 34px; top: 218px; font-size: 14px; line-height: 22px; }
  .contact__row { display: flex; align-items: center; justify-content: flex-end; gap: 10px; }
  .contact__row svg { width: 12px; height: 12px; fill: var(--text-light); }

  /* back */
  .card--back .brand { left: 92px; top: 96px; }
  .card--back .brand__name { font-size: 34px; width: 340px; }
  .card--back .brand__tagline { left: 118px; top: 182px; font-size: 14px; }
  .card__icon {
    position: absolute; left: 243px; top: 222px; width: 54px; height: 44px;
    background: var(--blue); border-radius: 8px;
  }
</style>
</head>
<body>
<main class="canvas">

  <section class="card card--front">
    <svg class="card__bands" viewBox="0 0 540 309" aria-hidden="true">
      <defs>
        <linearGradient id="greenBand" x1="0" y1="0" x2="1" y2="1">
          <stop offset="0" stop-color="var(--green-dark)"/>
          <stop offset="1" stop-color="var(--green)"/>
        </linearGradient>
        <linearGradient id="blueBand" x1="0" y1="0" x2="1" y2="1">
          <stop offset="0" stop-color="var(--blue)"/>
          <stop offset="1" stop-color="var(--blue-dark)"/>
        </linearGradient>
      </defs>
      <polygon points="250,0 540,0 540,80 320,150" fill="url(#greenBand)"/>
      <polygon points="320,150 540,80 540,309 300,309" fill="url(#blueBand)"/>
    </svg>

    <div class="brand">
      <span class="brand__mark"></span>
      <span class="brand__name">Carl Benson Insurance Agency</span>
    </div>
    <p class="brand__tagline">Serving Orchard Lane Since 1958</p>

    <p class="contact contact__name">Employee name</p>
    <div class="contact contact__phones">
      <div class="contact__row">0750-4821736
        <svg viewBox="0 0 24 24"><path d="M4 8c0-3 3-4 8-4s8 1 8 4v2h-4V8H8v2H4zM6 12h12l2 8H4z"/></svg>
      </div>
      <div class="contact__row">050-3917254
        <svg viewBox="0 0 24 24"><path d="M6 2l4 4-2 3c1 3 4 6 7 7l3-2 4 4-3 4C10 22 2 14 2 5z"/></svg>
      </div>
    </div>
    <div class="contact contact__online">
      <div class="contact__row">carl@bensoninsure.com
        <svg viewBox="0 0 24 24"><path d="M2 5h20v14H2zM4 7v1l8 5 8-5V7z"/></svg>
      </div>
      <div class="contact__row">www.carlbensonagency.com
        <svg viewBox="0 0 24 24"><circle cx="12" cy="12" r="10"/></svg>
      </div>
    </div>
  </section>

  <section class="card card--back">
    <div class="brand">
      <span class="brand__mark"></span>
      <span class="brand__name">Carl Benson Insurance Agency</span>
    </div>
    <p class="brand__tagline">Serving Orchard Lane Since 1958</p>
    <div class="card__icon" role="img" aria-label="Icon of two hands sheltering a house"></div>
  </section>

</main>
</body>
</html>
```